Health & Fitness Retreat Homepage Design

We have an existing website at http://www.BluePineHavens.com.au which we are retaining but wish to have a freshly designed homepage with the existing top navigation bar.
Sample layout is attached, but feel free to use your creativity on layout and colours, always remembering it needs to fit with the wider site design.
Project Delivery:
5 phase slide slow at top of homepage
Full homepage design and associated files
Target Audience:
- Female 80%, Male 20%
- Aged 30 to 50
- Overweight/Obese (so no pictures of thin people)
See attached layout for more information.
Target Market(s)
Target Audience:
- Female 80%, Male 20%
- Aged 30 to 50
Industry/Entity Type
Fitness
Requirements
Must have
- Must have existing top navigation bar as at http://www.BluePineHavens.com.au and fit with existing interior colours, etc.
Should not have
- No pictures of thin people

```html
<!DOCTYPE html>
<html lang="en">
<head>
<meta charset="utf-8">
<title>BluePineHavens – Weight Loss Retreat</title>
<link href="https://fonts.googleapis.com/css2?family=Roboto+Condensed:wght@400;700&family=Arimo:wght@400;700&display=swap" rel="stylesheet">
<style>
:root{
  --green:#6cb520;
  --green-dark:#5a9a18;
  --orange:#f28a30;
  --orange-dark:#e06d16;
  --red:#e8262c;
  --blue:#1a9ad6;
  --blue-dark:#1b6fb1;
  --navy:#1c5aa0;
  --text:#333;
  --grey:#555;
  --light:#e9eaec;
  --yellow:#ffe100;
}
*{box-sizing:border-box;margin:0;padding:0}
html,body{width:769px;height:1200px;overflow:hidden;background:#fff}
body{position:relative;font-family:"Arimo",Arial,sans-serif;color:var(--text)}
.abs{position:absolute}
.cond{font-family:"Roboto Condensed","Arial Narrow",sans-serif}

/* header */
.brand{left:57px;top:26px;display:flex;align-items:center;gap:8px}
.brand-dot{width:24px;height:24px;border-radius:50%;background:var(--orange)}
.brand-name{font-family:"Roboto Condensed",sans-serif;font-weight:700;font-size:25px;color:var(--green)}
.nav-col{top:10px;width:88px}
.nav-col h4{font-size:7px;font-weight:700;color:#333;border-bottom:1px solid #ccc;padding-bottom:4px;margin-bottom:4px;letter-spacing:.1px}
.nav-col li{list-style:none;font-size:5.6px;color:#666;line-height:11px;padding-left:9px;position:relative}
.nav-col li::before{content:"";position:absolute;left:1px;top:4px;border-left:3px solid var(--orange);border-top:2px solid transparent;border-bottom:2px solid transparent}
.mag{left:633px;top:6px;width:80px}
.mag-cover{position:absolute;left:0;top:0;width:24px;height:44px;background:linear-gradient(#d9534f,#c77b55 50%,#6b8b4a)}
.mag-title{position:absolute;left:36px;top:2px;font-family:"Roboto Condensed",sans-serif;font-weight:700;font-size:8px;line-height:8px;color:#222}
.mag-title b{color:var(--red);font-size:11px}
.mag-req{position:absolute;left:24px;top:32px;background:#444;color:#fff;font-size:6px;font-weight:700;padding:2px 3px}
.mag-btn{position:absolute;left:2px;top:51px;width:76px;height:16px;background:var(--blue);border:2px solid #cfe3f2;color:#fff;font-family:"Roboto Condensed",sans-serif;font-weight:700;font-size:8.5px;text-align:center;line-height:12px}

/* slider */
.slider{left:57px;top:92px;width:655px;height:257px;border:1px solid #ccc;border-radius:4px;padding:4px}
.slide{position:relative;width:100%;height:100%;background:var(--light)}
.slide-photo{position:absolute;right:0;top:0;width:345px;height:100%;background:linear-gradient(90deg,#e3e3e5,#c9987f 25%,#d8a890 55%,#4a5a7a 85%,#c7c8cb)}
.slide-copy{position:absolute;left:73px;top:80px}
.slide-copy h1{font-family:"Roboto Condensed",sans-serif;font-weight:700;font-size:21px;color:var(--green)}
.slide-copy .sub{font-family:"Roboto Condensed",sans-serif;font-style:italic;font-weight:700;font-size:10px;color:var(--orange);margin:2px 0 7px}
.slide-copy li{list-style:none;font-family:"Roboto Condensed",sans-serif;font-weight:700;font-size:9.5px;color:var(--navy);line-height:16px;padding-left:11px;position:relative}
.slide-copy li::before{content:"";position:absolute;left:0;top:4px;border-left:5px solid var(--navy);border-top:3px solid transparent;border-bottom:3px solid transparent}
.slide-btn{margin-top:10px;display:inline-block;width:151px;height:29px;border-radius:15px;background:linear-gradient(#f78e3c,#e8262c);color:#fff;font-family:"Roboto Condensed",sans-serif;font-weight:700;font-size:12px;text-align:center;line-height:29px;box-shadow:0 0 0 3px #d8d8d8}
.dots{position:absolute;right:28px;bottom:9px;display:flex;gap:4px;background:rgba(0,0,0,.25);border-radius:8px;padding:2px 4px}
.dots i{width:10px;height:10px;border-radius:50%;background:#fff;display:block}
.dots i.on{background:var(--orange)}

/* offer */
.offer{left:57px;top:358px;width:432px;height:28px;background:var(--red);color:#fff;font-family:"Roboto Condensed",sans-serif;font-weight:700;font-size:15px;line-height:28px;padding-left:24px}
.offer .hl{color:var(--yellow)}
.offer u{color:var(--yellow);margin-left:4px}

/* cards */
.card{top:404px;width:128px}
.card-head{height:38px;font-family:"Roboto Condensed",sans-serif;font-weight:700;font-size:9.5px;text-align:center;color:#222;line-height:15px;padding-top:5px;border-radius:3px 3px 0 0}
.card-photo{height:77px;border-radius:0 0 3px 3px}
.card p{font-size:8.6px;line-height:15.5px;color:#333;margin-top:4px}
.card a{display:block;font-size:7px;line-height:13px;color:var(--orange);text-decoration:underline;margin-top:1px}

/* home box */
.home{left:57px;top:614px;width:432px;height:63px;background:var(--orange);border-radius:3px;color:#fff}
.home .pre{position:absolute;left:25px;top:8px;font-size:10px;font-weight:700}
.home .big{position:absolute;left:23px;top:23px;font-family:"Roboto Condensed",sans-serif;font-weight:700;font-size:16.5px;color:#3a2a1f}
.home .small{position:absolute;left:25px;top:46px;font-size:8.5px;color:#3a2a1f}
.home-photo{position:absolute;right:6px;top:3px;width:90px;height:56px;background:linear-gradient(90deg,#7b8a8a,#c9c8b9 45%,#9a6a4a 70%,#4a4f5a)}

/* main text */
.main h2{font-family:"Roboto Condensed",sans-serif;font-weight:700;font-size:15px;color:var(--green-dark)}
.main .tag{font-size:9.6px;color:#444}
.rule{left:57px;width:432px;height:1px;background:#ddd}
.para{left:62px;width:420px;font-size:10.3px;line-height:16px;color:#444}
.more{left:61px;font-size:7.8px;color:var(--orange);text-decoration:underline}
.callbtn{left:60px;width:256px;height:26px;background:var(--orange);border-radius:2px;color:#fff;font-size:9.3px;font-weight:700;line-height:26px;padding-left:12px}
.callbtn u{color:#3a2a1f}
.ticks{left:62px;width:420px}
.ticks li{list-style:none;font-size:10.3px;line-height:16.2px;color:#444;padding-left:16px;position:relative}
.ticks svg{position:absolute;left:0;top:4px}

/* green column */
.green{left:508px;top:358px;width:204px;height:467px;background:var(--green);border-radius:2px}
.green h3{position:absolute;left:14px;top:13px;width:185px;font-family:"Roboto Condensed",sans-serif;font-weight:700;font-size:10px;line-height:13.5px;color:#fff}
.green .link{position:absolute;left:14px;top:47px;font-size:7px;font-weight:700;color:#fff;text-decoration:underline}
.video{position:absolute;left:17px;top:64px;width:174px;height:114px;border:2px solid #fff}
.video-img{position:absolute;inset:0 0 8px 0;background:linear-gradient(#bcd0e2,#8ea2a9 45%,#55683e 70%,#3d4d5a)}
.video-play{position:absolute;left:70px;top:35px}
.video-bar{position:absolute;left:0;right:0;bottom:0;height:8px;background:#2b2b2b}
.video-bar i{position:absolute;left:30px;right:46px;top:3px;height:2px;background:#777}
.glist{position:absolute;left:17px;top:189px;width:184px}
.glist li{list-style:none;font-size:6.5px;font-weight:700;color:#fff;line-height:10.4px;padding-left:12px;position:relative;margin-bottom:4.6px}
.glist svg{position:absolute;left:0;top:2px}
.green .gbtn{position:absolute;left:30px;top:419px;width:142px;height:37px;background:linear-gradient(var(--orange),#ec5a1c);color:#fff;font-size:9px;font-weight:700;line-height:13px;padding:7px 0 0 12px}

/* programs */
.programs{left:508px;top:833px;width:204px;height:93px;background:var(--orange);border-radius:2px;overflow:hidden}
.programs h3{height:26px;background:#555;color:#fff;font-family:"Roboto Condensed",sans-serif;font-weight:700;font-size:12px;text-align:center;line-height:26px}
.programs a{display:block;margin-left:18px;font-size:8.2px;font-weight:700;color:var(--blue-dark);text-decoration:underline;line-height:18px}
.programs a:first-of-type{margin-top:3px}

/* contact */
.contact{left:508px;top:935px;width:204px;height:260px;background:var(--blue);border-radius:2px;overflow:hidden}
.contact h3{height:30px;background:var(--blue-dark);color:#fff;font-family:"Roboto Condensed",sans-serif;font-weight:700;font-size:13px;text-align:center;line-height:30px}
.field{position:absolute;left:17px;width:170px;height:19px;background:#fff;border-radius:2px;font-size:7.8px;color:#888;line-height:19px;padding-left:7px}
.field.area{height:62px;line-height:16px;padding-top:2px}
.submit{position:absolute;right:21px;top:221px;width:86px;height:19px;background:var(--red);border-radius:2px;color:#fff;font-size:9.5px;font-weight:700;text-align:center;line-height:19px}
</style>
</head>
<body>

<header>
  <div class="abs brand"><span class="brand-dot"></span><span class="brand-name">BluePineHavens</span></div>

  <nav class="abs nav-col" style="left:298px">
    <h4>THE BEST PROGRAMS</h4>
    <ul><li>Weight Loss Retreat</li><li>Fitness Camps</li><li>Home Retreat</li></ul>
  </nav>
  <nav class="abs nav-col" style="left:405px">
    <h4>THE BEST LOCATIONS</h4>
    <ul><li>Blue Mountains, NSW</li><li>Central Coast, NSW</li><li>Victoria (Torquay)</li></ul>
  </nav>
  <nav class="abs nav-col" style="left:514px">
    <h4>ABOUT BLUEPINE</h4>
    <ul><li>Why choose BluePine</li><li>What clients say....</li><li>Contact us</li><li>FREE Brochure</li><li>Special Offers</li></ul>
  </nav>

  <div class="abs mag">
    <div class="mag-cover" role="img" aria-label="Magazine cover with smiling woman"></div>
    <div class="mag-title"><b>FREE</b><br>BLUEPINE<br>MAGAZINE</div>
    <div class="mag-req">REQUEST NOW!</div>
    <div class="mag-btn">FREE BROCHURE</div>
  </div>
</header>

<section class="abs slider">
  <div class="slide">
    <div class="slide-photo" role="img" aria-label="Two women in lingerie showing weight loss results in oversized jeans"></div>
    <div class="slide-copy">
      <h1>Transform your Body &amp; Life</h1>
      <p class="sub">At Australia´s No. 1 Weight Loss &amp; Fitness Retreat</p>
      <ul><li>For All Shapes, Sizes &amp; Fitness Levels</li><li>Stunning Locations &amp; 1st Class Facilities</li><li>Amazing Weight Loss Results</li></ul>
      <span class="slide-btn">REQUEST A BROCHURE</span>
    </div>
    <div class="dots"><i class="on"></i><i></i><i></i><i></i><i></i></div>
  </div>
</section>

<div class="abs offer"><span class="hl">SPECIAL OFFER:</span> 2 for 1 at the Blue Mountain. <u>View Offers &gt;&gt;</u></div>

<article class="abs card" style="left:62px">
  <div class="card-head" style="background:#9fcdee">BLUE MOUNTAIN SYDNEY<br>WEIGHT LOSS RETREAT</div>
  <div class="card-photo" role="img" aria-label="Blue Mountains rock formation at sunset" style="background:linear-gradient(#b9a0c9,#e9a56f 40%,#7a5a2e 65%,#34401f)"></div>
  <p>Praesent vestibulum molestie lacus. Aenean ummy hendrerit mauris. Phasellus porta.</p>
  <a>Blue Mountain Sydney Weight Loss Retreat &gt;&gt;</a>
</article>
<article class="abs card" style="left:212px">
  <div class="card-head" style="background:var(--orange)">CENTRAL COAST NSW<br>WEIGHT LOSS RETREAT</div>
  <div class="card-photo" role="img" aria-label="Rocky coastline with waves at dusk" style="background:linear-gradient(#5a7a9a,#c59a84 40%,#e8d9cc 55%,#3a3230)"></div>
  <p>Praesent vestibulum molestie lacus. Aenean ummy hendrerit mauris. Phasellus porta.</p>
  <a>Central Coast NSW Weight Loss Retreat &gt;&gt;</a>
</article>
<article class="abs card" style="left:362px">
  <div class="card-head" style="background:#bde08a">VICTORIA WEIGHT LOSS<br>HEALTH RETREATS</div>
  <div class="card-photo" role="img" aria-label="Modern bright retreat interior" style="background:linear-gradient(90deg,#dde0e3,#f2f2f2 40%,#9aa3ab 70%,#e5e7ea)"></div>
  <p>Praesent vestibulum molestie lacus. Aenean ummy hendrerit mauris. Phasellus porta.</p>
  <a>Victoria Weight Loss Health Retreats &gt;&gt;</a>
</article>

<section class="abs home">
  <span class="pre">...or let us come to you</span>
  <span class="big">HOME WEIGHT LOSS &amp; FITNESS PROGRAM &gt;&gt;</span>
  <span class="small">Aliquam congue fermentum Mauris accumsan nulla vel.</span>
  <div class="home-photo" role="img" aria-label="Woman choosing food from an open fridge"></div>
</section>

<section class="main">
  <div class="abs" style="left:62px;top:697px">
    <h2>Weight Loss Retreats, Health Retreats and Weight Loss Camps</h2>
    <p class="tag">For adults of all ages, shapes, sizes and fitness levels.</p>
  </div>
  <div class="abs rule" style="top:732px"></div>
  <p class="abs para" style="top:741px">Praesent vestibulum molestie lacus. Aenean ummy hendrerit mauris. Phasellus porta. Fusce suscipit varius mi. Aliquam congue fermentum maris accumsan nulla vel, praesent vestibulum molestie lacus, aenean ummy hendrerit mauris. Phasellus porta, fusce suscipit varius mi. Aliquem congue fermentum maris accumsan nulla vel, praesent vestibulum molestie lacus, aenean ummy hendrerit mauris. Phasellus port, fusce suscipit varius mi. Aliquem congue fermentum maris accumsan nulla vel.</p>
  <a class="abs more" style="top:845px">Read more about the Weight Loss Retreat Program here &gt;&gt;</a>
  <div class="abs callbtn" style="top:872px">Call: 1300 555 018 or <u>Request a Brochure &gt;&gt;</u></div>

  <h2 class="abs" style="left:59px;top:915px">The Most Comprehensive Weight Loss Retreats in Australia</h2>
  <ul class="abs ticks" style="top:938px">
    <li><svg width="9" height="8" viewBox="0 0 9 8"><path d="M1 4l2.5 2.5L8 1" stroke="#1b6fb1" stroke-width="1.8" fill="none"/></svg>Praesent vestibulum molestie lacus.</li>
    <li><svg width="9" height="8" viewBox="0 0 9 8"><path d="M1 4l2.5 2.5L8 1" stroke="#1b6fb1" stroke-width="1.8" fill="none"/></svg>Aenean ummy hendrerit mauris. Phasellus porta.</li>
    <li><svg width="9" height="8" viewBox="0 0 9 8"><path d="M1 4l2.5 2.5L8 1" stroke="#1b6fb1" stroke-width="1.8" fill="none"/></svg>Fusce suscipit varius mi. Aliquam congue fermentum maris accumsan nulla vel.</li>
    <li><svg width="9" height="8" viewBox="0 0 9 8"><path d="M1 4l2.5 2.5L8 1" stroke="#1b6fb1" stroke-width="1.8" fill="none"/></svg>Phasellus porta,fusce suscipit varius mi.</li>
  </ul>
  <p class="abs para" style="top:1014px">Praesent vestibulum molestie lacus. Aenean ummy hendrerit mauris. Phasellus porta. Fusce suscipit varius mi. Aliquam congue fermentum maris accumsan nulla vel, praesent vestibulum molestie lacus, aenean ummy hendrerit mauris. Phasellus porta, fusce suscipit varius mi. Aliquem congue fermentum maris accumsan nulla vel, praesent vestibulum molestie lacus, aenean ummy hendrerit mauris. Phasellus port, fusce suscipit varius mi. Aliquem congue fermentum maris accumsan nulla vel.</p>
  <a class="abs more" style="top:1118px">Read more about the Weight Loss Retreat Program here &gt;&gt;</a>
  <div class="abs callbtn" style="top:1143px">Call: 1300 555 018 or <u>Request a Brochure &gt;&gt;</u></div>
</section>

<aside class="abs green">
  <h3>Change your Life at Australia´s most popular Weight Loss &amp; Fitness Retreat</h3>
  <span class="link">More about the Program &gt;&gt;</span>
  <div class="video">
    <div class="video-img" role="img" aria-label="Video still of a woman sitting by a lake"></div>
    <svg class="video-play" width="32" height="32" viewBox="0 0 32 32"><circle cx="16" cy="16" r="16" fill="#111"/><path d="M12 9l11 7-11 7z" fill="#fff"/></svg>
    <div class="video-bar"><i></i></div>
  </div>
  <ul class="glist">
    <li><svg width="8" height="7" viewBox="0 0 8 7"><path d="M1 3.5l2 2L7 1" stroke="#fff" stroke-width="1.6" fill="none"/></svg>Praesent vestibulum molestie lacus. Aenean ummy hendrerit mauris. Phasellus porta.</li>
    <li><svg width="8" height="7" viewBox="0 0 8 7"><path d="M1 3.5l2 2L7 1" stroke="#fff" stroke-width="1.6" fill="none"/></svg>Praesent vestibulum molestie lacus.</li>
    <li><svg width="8" height="7" viewBox="0 0 8 7"><path d="M1 3.5l2 2L7 1" stroke="#fff" stroke-width="1.6" fill="none"/></svg>Praesent vestibulum molestie lacus. Aenean ummy hendrerit mauris. Phasellus porta.</li>
    <li><svg width="8" height="7" viewBox="0 0 8 7"><path d="M1 3.5l2 2L7 1" stroke="#fff" stroke-width="1.6" fill="none"/></svg>Praesent vestibulum molestie lacus. Aenean ummy hendrerit mauris. Phasellus porta.</li>
    <li><svg width="8" height="7" viewBox="0 0 8 7"><path d="M1 3.5l2 2L7 1" stroke="#fff" stroke-width="1.6" fill="none"/></svg>Praesent vestibulum molestie lacus. Aenean ummy hendrerit mauris. Phasellus porta.</li>
    <li><svg width="8" height="7" viewBox="0 0 8 7"><path d="M1 3.5l2 2L7 1" stroke="#fff" stroke-width="1.6" fill="none"/></svg>Praesent vestibulum molestie lacus. Aenean ummy hendrerit mauris. Phasellus porta.</li>
    <li><svg width="8" height="7" viewBox="0 0 8 7"><path d="M1 3.5l2 2L7 1" stroke="#fff" stroke-width="1.6" fill="none"/></svg>Praesent vestibulum molestie lacus. Aenean ummy hendrerit mauris. Phasellus porta.</li>
    <li><svg width="8" height="7" viewBox="0 0 8 7"><path d="M1 3.5l2 2L7 1" stroke="#fff" stroke-width="1.6" fill="none"/></svg>Praesent vestibulum molestie lacus. Aenean ummy hendrerit mauris. Phasellus porta.</li>
    <li><svg width="8" height="7" viewBox="0 0 8 7"><path d="M1 3.5l2 2L7 1" stroke="#fff" stroke-width="1.6" fill="none"/></svg>Praesent vestibulum molestie lacus. Aenean ummy hendrerit mauris. Phasellus porta.</li>
    <li><svg width="8" height="7" viewBox="0 0 8 7"><path d="M1 3.5l2 2L7 1" stroke="#fff" stroke-width="1.6" fill="none"/></svg>Praesent vestibulum molestie lacus.</li>
  </ul>
  <div class="gbtn">Call: 1300 555 018 or<br>Request a Brochure &gt;&gt;</div>
</aside>

<aside class="abs programs">
  <h3>Other Programs Available:</h3>
  <a>Fitness Camps &amp; Fitness Retreats &gt;&gt;</a>
  <a>Stop Emotional Eating Worshop &gt;&gt;</a>
  <a>VIP Private Retreats Worldwide &gt;&gt;</a>
</aside>

<aside class="abs contact">
  <h3>Contact Us</h3>
  <div class="field" style="top:37px">Name</div>
  <div class="field" style="top:61px">Email</div>
  <div class="field" style="top:85px">Phone Number</div>
  <div class="field" style="top:109px">Current Weight</div>
  <div class="field" style="top:133px">Closest City</div>
  <div class="field area" style="top:157px">Comment</div>
  <div class="submit">Submit Details</div>
</aside>

</body>
</html>
```